Bourbon label design for bourbon brand. Looking to freshen our current label.

I need a Bourbon label design for our rebranded Bourbon bottle. Label should include picture of our horse and our logo on the bottle. Front Label is 3.5 inches wide and 6 inches tall, back label is 4 inches tall and 3 inches wide. Back label can be a simple plain logo like the one in the brief. I have included a design of our current bottle and label. We want to stay close to the current color schemes but want a fresh rebrand of the design. The label needs to be the correct size on a tall bottle like pictured.

Target Market(s)

Our Bourbon members, 30-50 year old males

Requirements
Must have
• Picture of our horse, our DARKRUN , straight Bourbon whiskey on the front. Room to edit text on the back label.

```html
<!DOCTYPE html>
<html lang="en">
<head>
<meta charset="utf-8">
<title>Darkrun Straight Whiskey – Front Label</title>
<link rel="stylesheet" href="https://fonts.googleapis.com/css2?family=Big+Shoulders+Display:wght@200&family=Big+Shoulders+Inline+Display:wght@700&family=Playfair+Display:wght@700;900&display=swap">
<style>
  :root {
    --backdrop: #d9d9db;
    --label-black: #050505;
    --ink-white: #ffffff;
    --ink-grey: #a9a9a9;
    --ink-dim: #5e5e5e;
    --field-grey: #d8d8d8;
    --art-light: #6b635c;
    --art-dark: #1a1715;
  }
  * { margin: 0; padding: 0; box-sizing: border-box; }
  html, body { width: 1200px; height: 1200px; overflow: hidden; }
  body { background: var(--backdrop); position: relative; }

  .front-label {
    position: absolute; left: 230px; top: 45px;
    width: 740px; height: 1110px;
    background: var(--label-black);
    color: var(--ink-white);
    font-family: "Playfair Display", Georgia, serif;
  }
  .front-label > * { position: absolute; }

  .brand-mark {
    top: 110px; left: 0; width: 100%;
    text-align: center;
    font-weight: 900; font-size: 44px; letter-spacing: 6px;
  }

  .horse-art {
    left: 208px; top: 258px; width: 340px; height: 680px;
    border-radius: 45% 45% 30% 30%;
    background: radial-gradient(ellipse at 50% 40%, var(--art-light) 0%, #3b3631 45%, var(--art-dark) 75%, var(--label-black) 100%);
  }

  .est-mark {
    top: 360px; width: 60px; height: 64px;
    border-top: 1px solid var(--ink-dim); border-bottom: 1px solid var(--ink-dim);
    font-family: "Big Shoulders Display", "Arial Narrow", sans-serif;
    font-weight: 200; font-size: 38px; line-height: 62px;
    color: var(--ink-dim); text-align: center;
  }
  .est-mark--left { left: 70px; }
  .est-mark--right { right: 60px; width: 70px; }

  .product-name {
    top: 560px; left: 0; width: 100%;
    text-align: center;
    font-family: "Big Shoulders Inline Display", Impact, sans-serif;
    font-weight: 700; font-size: 150px; line-height: 150px;
    letter-spacing: 2px;
  }

  .product-type {
    top: 730px; left: 0; width: 100%;
    text-align: center;
    font-size: 19px; letter-spacing: 6px;
  }

  .side-note {
    top: 822px;
    font-size: 16px; line-height: 21px; letter-spacing: 3px;
    color: var(--ink-grey);
  }
  .side-note--left { left: 115px; }
  .side-note--right { right: 115px; text-align: center; }

  .detail-caption {
    font-size: 15px; letter-spacing: 2px; color: var(--ink-grey);
    text-align: center;
  }
  .caption-batch { left: 184px; top: 993px; width: 110px; }
  .caption-aged { left: 318px; top: 968px; width: 89px; }
  .caption-alc { left: 426px; top: 993px; width: 110px; }
  .caption-years { left: 308px; top: 1076px; width: 109px; }

  .detail-field { background: var(--field-grey); }
  .field-batch { left: 204px; top: 1017px; width: 70px; height: 38px; }
  .field-aged { left: 318px; top: 995px; width: 89px; height: 76px; }
  .field-alc { left: 446px; top: 1017px; width: 70px; height: 38px; }
</style>
</head>
<body>
  <section class="front-label">
    <div class="brand-mark">DARKRUN</div>

    <div class="horse-art" role="img" aria-label="Engraved-style illustration of a racehorse and jockey galloping toward the viewer, number 4 on the saddle cloth"></div>

    <div class="est-mark est-mark--left">EST</div>
    <div class="est-mark est-mark--right">2021</div>

    <h1 class="product-name">DARKRUN</h1>
    <p class="product-type">AMERICAN STAIGTH WHISKEY</p>

    <p class="side-note side-note--left">SMALL<br>BATCH</p>
    <p class="side-note side-note--right">CASK<br>STRENGTH</p>

    <span class="detail-caption caption-batch">BATCH NO.</span>
    <span class="detail-caption caption-aged">AGED</span>
    <span class="detail-caption caption-alc">ALC/VOL</span>
    <div class="detail-field field-batch"></div>
    <div class="detail-field field-aged"></div>
    <div class="detail-field field-alc"></div>
    <span class="detail-caption caption-years">YEARS</span>
  </section>
</body>
</html>
```